Word document template for sales proposals

I am after a template that is simple but impactful. Use of colour to be limited but some for impact would be good. The proposals are for use in the professional technical field.

```html
<!DOCTYPE html>
<html lang="en">
<head>
<meta charset="utf-8">
<title>Sales Proposal Template – NORVEL</title>
<link href="https://fonts.googleapis.com/css2?family=Poppins:wght@300;400;500;600;700;800&display=swap" rel="stylesheet">
<style>
:root{
  --stage:#474747;
  --paper:#ffffff;
  --orange:#f0962a;
  --blue:#2aa9e0;
  --sky:#addceb;
  --sky-soft:#d7eef6;
  --ink:#2b2b2b;
  --grey:#8a8a8a;
  --faint:#d9d9d9;
  --brand-ghost:#5b5b5b;
}
*{margin:0;padding:0;box-sizing:border-box}
html,body{width:1200px;height:943px;overflow:hidden;background:var(--stage);font-family:"Poppins",sans-serif;color:var(--ink)}
.canvas{position:relative;width:1200px;height:943px}
.page{position:absolute;background:var(--paper);overflow:hidden}
.abs{position:absolute}
.tiny{font-size:2.4px;line-height:3.2px;color:#555}
.small{font-size:3.2px;line-height:4px;color:#555}
.title{font-size:8.5px;line-height:8.5px;font-weight:300;color:#444}
.title b{display:block;font-weight:700;color:var(--orange)}
.photo{position:absolute}
.footer-band{position:absolute;left:0;bottom:3px;width:35px;height:7px;background:var(--blue)}
.footer-mark{position:absolute;left:28px;bottom:2px;width:9px;height:9px;border-radius:50%;background:#fff;border:1px solid var(--blue)}
.footer-text{position:absolute;left:0;right:0;bottom:4px;text-align:center;font-size:2.4px;line-height:3px;color:#555}
.footer-num{position:absolute;right:0;bottom:3px;width:28px;height:7px;background:var(--orange);color:#fff;font-size:3px;line-height:7px;text-align:center}
.ghost-name{font-weight:700;color:#cfe8f2;letter-spacing:1px}
.brand{font-weight:700;color:var(--blue);letter-spacing:.5px}
.bar{position:absolute;background:var(--blue);color:#fff;font-size:2.8px;line-height:7px;padding-left:5px}
.drop{position:absolute;width:5px;height:5px;border-radius:50%;background:var(--orange)}
.dot-blue{position:absolute;width:5px;height:5px;border-radius:50%;background:var(--blue);color:#fff;font-size:2.6px;line-height:5px;text-align:center}
/* cover */
.cover .sales{left:22px;top:20px;font-size:26px;font-weight:300;line-height:26px}
.cover .proposal{left:22px;top:45px;font-size:26px;font-weight:700;line-height:28px}
.cover .rule{left:24px;top:89px;width:18px;height:1.5px;background:var(--orange)}
.meta-line{position:absolute;width:1.2px;height:13px;background:var(--orange)}
.meta{position:absolute;font-size:4.6px;line-height:5.4px;color:#9a9a9a}
.stage-name{position:absolute;left:232px;top:720px;font-size:80px;font-weight:800;color:var(--brand-ghost);letter-spacing:6px;line-height:80px}
</style>
</head>
<body>
<div class="canvas">

  <!-- COVER -->
  <section class="page cover" style="left:180px;top:179px;width:303px;height:423px">
    <svg class="abs" style="left:0;top:0" width="303" height="423" viewBox="0 0 303 423">
      <path d="M200 0H303V100Q303 112 290 106L210 66Q200 61 200 50Z" fill="#addceb"/>
      <g role="img" aria-label="Photo of white geometric lattice structure">
        <path d="M0 120H140Q150 120 160 126L303 205V250L265 325Q258 332 248 332H205Q195 332 185 326L0 236Z" fill="url(#lattice)"/>
      </g>
      <g role="img" aria-label="Orange-toned lattice detail">
        <path d="M0 222L85 262Q97 268 96 282L92 296Q88 308 75 302L0 268Z" fill="url(#warm)"/>
      </g>
      <defs>
        <linearGradient id="lattice" x1="0" y1="0" x2="1" y2="1"><stop offset="0" stop-color="#f2f2f2"/><stop offset=".5" stop-color="#bfbfbf"/><stop offset="1" stop-color="#e6e6e6"/></linearGradient>
        <linearGradient id="warm" x1="0" y1="0" x2="1" y2="1"><stop offset="0" stop-color="#f7d3a6"/><stop offset="1" stop-color="#ee8f24"/></linearGradient>
      </defs>
    </svg>
    <div class="abs brand" style="left:226px;top:28px;font-size:9px">NORVEL</div>
    <div class="abs" style="left:226px;top:40px;font-size:3px;color:var(--blue);letter-spacing:.3px">ENGINEERED LASTING RESULTS</div>
    <div class="abs sales">Sales</div>
    <div class="abs proposal">Proposal</div>
    <div class="abs rule"></div>
    <div class="abs" style="left:16px;top:307px;font-size:11px;font-weight:700;color:#ececec;letter-spacing:1px">NORVEL</div>
    <div class="abs" style="left:38px;top:325px;font-size:6px;color:#a0a0a0">Project # 110</div>
    <div class="abs" style="left:38px;top:333px;font-size:4.4px;color:#b0b0b0">Lorem ipsum dolor sit amet</div>
    <div class="abs" style="left:0;top:372px;width:90px;height:8px;background:var(--orange);border-radius:0 4px 4px 0;color:#fff;font-size:5.4px;font-weight:500;line-height:8px;padding-left:40px">Prepared for:</div>
    <div class="abs" style="left:41px;top:383px;font-size:6.4px;color:#9a9a9a">Heading of Company</div>
    <div class="abs" style="left:41px;top:391px;font-size:4.6px;color:#b0b0b0;line-height:6px">Lorem ipsum dolor sit amet<br>P: 12-123 1234 &nbsp;| &nbsp;E: info@xyx.com</div>
    <div class="meta-line" style="left:209px;top:372px"></div>
    <div class="meta" style="left:213px;top:372px">Proposal Issued:<br>16-10-2023</div>
    <div class="meta-line" style="left:209px;top:394px"></div>
    <div class="meta" style="left:213px;top:394px">Proposal Valid to:<br>28-10-2023</div>
  </section>

  <!-- TABLE OF CONTENT -->
  <section class="page" style="left:558px;top:32px;width:185px;height:261px">
    <div class="abs title" style="left:25px;top:17px">TABLE OF<b>CONTENT</b></div>
    <div class="abs" style="left:94px;top:39px;width:91px;height:18px;background:var(--sky);border-radius:9px 0 0 9px"></div>
    <div class="abs ghost-name" style="left:110px;top:42px;font-size:12px;color:#c5e4ef">NORVEL</div>
    <div class="abs" style="left:0;top:60px;width:72px;height:157px;background:var(--sky);border-radius:0 0 12px 0"></div>
    <div class="abs" style="left:14px;top:125px;width:26px;height:26px;border-radius:50%;border:2px solid #c7e6f1"></div>
    <div class="abs" style="left:62px;top:73px;font-size:9px;color:var(--orange);line-height:13.6px;text-align:right;width:8px;font-weight:300">1<br>3<br>6<br>10</div>
    <div class="abs tiny" style="left:75px;top:76px">Lorem ipsum dolor sit amet, consectetur</div>
    <div class="abs tiny" style="left:75px;top:90px">Lorem ipsum dolor sit amet, consectetur</div>
    <div class="abs tiny" style="left:75px;top:101px">Lorem ipsum dolor sit amet, lorem ipsum<br>dolor sit amet, consectetur</div>
    <div class="abs tiny" style="left:75px;top:118px">Lorem ipsum dolor sit amet, lorem ipsum<br>dolor sit amet, consectetur</div>
    <div class="footer-band"></div><div class="footer-mark"></div>
    <div class="footer-text">NORVEL LASTING RESULTS<br>Lorem ipsum dolor sit amet | P: 12-123 1234 | E: info@xyx.com</div>
    <div class="footer-num">12</div>
  </section>

  <!-- CASE STUDIES -->
  <section class="page" style="left:757px;top:32px;width:185px;height:261px">
    <div class="abs title" style="left:16px;top:12px">CASE<b>STUDIES</b></div>
    <div class="abs" style="left:0;top:30px;width:96px;height:70px;background:var(--orange);border-radius:0 10px 10px 0"></div>
    <div class="abs" style="left:23px;top:55px;font-size:8px;line-height:9px;font-weight:300;color:#5a3a10">PROJECT<br>PROPOSAL</div>
    <div class="photo" role="img" aria-label="Photo looking up at tall forest trees" style="left:98px;top:31px;width:87px;height:70px;border-radius:12px 0 0 0;background:linear-gradient(135deg,#2f5d4c,#7fa38e 50%,#2c4a3a)"></div>
    <div class="abs tiny" style="left:12px;top:119px;width:160px">Lorem ipsum dolor sit amet, consectetur adipiscing elit, sed do eiusmod tempor incididunt ut labore et dolore magna aliqua. Ut enim ad minim veniam, quis nostrud exercitation ullamco laboris nisi ut aliquip ex ea commodo consequat. Duis aute irure dolor in reprehenderit in voluptate velit esse cillum dolore eu fugiat nulla pariatur.</div>
    <div class="photo" role="img" aria-label="Black and white photo of a person standing on a rocky shore" style="left:0;top:149px;width:82px;height:80px;background:linear-gradient(180deg,#d9d9d9,#9a9a9a 55%,#4a4a4a)"></div>
    <div class="drop" style="left:79px;top:155px;width:9px;height:9px"></div>
    <div class="drop" style="left:79px;top:180px;width:9px;height:9px"></div>
    <div class="drop" style="left:79px;top:205px;width:9px;height:9px"></div>
    <div class="abs tiny" style="left:95px;top:155px;width:80px">Lorem ipsum dolor sit amet, consectetur adipiscing elit, sed do eiusmod tempor incididunt ut labore et dolore magna aliqua. Ut enim ad minim veniam, quis nostrud.</div>
    <div class="abs tiny" style="left:95px;top:180px;width:80px">Lorem ipsum dolor sit amet, consectetur adipiscing elit, sed do eiusmod tempor incididunt ut labore et dolore magna aliqua. Ut enim ad minim veniam, quis nostrud.</div>
    <div class="abs tiny" style="left:95px;top:205px;width:80px">Lorem ipsum dolor sit amet, consectetur adipiscing elit, sed do eiusmod tempor incididunt ut labore et dolore magna aliqua. Ut enim ad minim veniam, quis nostrud.</div>
    <div class="footer-band"></div><div class="footer-mark"></div>
    <div class="footer-text">NORVEL LASTING RESULTS<br>Lorem ipsum dolor sit amet | P: 12-123 1234 | E: info@xyx.com</div>
    <div class="footer-num">12</div>
  </section>

  <!-- PROPOSAL FOR PROJECT -->
  <section class="page" style="left:958px;top:32px;width:185px;height:261px">
    <div class="abs" style="left:1px;top:22px;width:3px;height:6px;background:var(--blue)"></div>
    <div class="abs title" style="left:13px;top:12px">PROPOSAL FOR<b>PROJECT</b></div>
    <div class="abs tiny" style="left:13px;top:37px;width:95px">Lorem ipsum dolor sit amet, consectetur adipiscing elit, sed do eiusmod tempor incididunt ut labore et dolore magna aliqua. Ut enim ad minim veniam, quis nostrud exercitation ullamco.</div>
    <div class="photo" role="img" aria-label="Photo of hands holding soil" style="left:117px;top:10px;width:68px;height:41px;border-radius:9px 0 0 0;background:linear-gradient(135deg,#6b5a48,#3a2d22 60%,#c0762e)"></div>
    <div class="abs" style="left:16px;top:63px;width:47px;height:39px;background:var(--orange)"></div>
    <div class="abs" style="left:68px;top:63px;width:47px;height:39px;background:var(--orange)"></div>
    <div class="abs" style="left:120px;top:63px;width:47px;height:39px;background:var(--orange)"></div>
    <div class="abs" style="left:16px;top:110px;font-size:6px;line-height:7px;font-weight:300;color:#444">PROPOSAL<br>NAME HERE</div>
    <div class="abs" style="left:68px;top:110px;font-size:6px;line-height:7px;font-weight:300;color:#444">PROPOSAL<br>NAME HERE</div>
    <div class="abs" style="left:120px;top:110px;font-size:6px;line-height:7px;font-weight:300;color:#444">PROPOSAL<br>NAME HERE</div>
    <div class="abs tiny" style="left:16px;top:134px;width:46px">Lorem ipsum dolor sit amet, consectetur adipiscing elit, sed do eiusmod tempor incididunt ut labore.</div>
    <div class="abs tiny" style="left:68px;top:134px;width:46px">Lorem ipsum dolor sit amet, consectetur adipiscing elit, sed do eiusmod tempor incididunt ut labore.</div>
    <div class="abs tiny" style="left:120px;top:134px;width:46px">Lorem ipsum dolor sit amet, consectetur adipiscing elit, sed do eiusmod tempor incididunt ut labore.</div>
    <div class="abs" style="left:15px;top:163px;font-size:6px;line-height:7px;font-weight:300;color:#444">PROPOSAL<br>DETAIL HERE</div>
    <div class="abs" style="left:92px;top:166px;width:93px;height:34px;background:var(--blue);border-radius:8px 0 0 8px"></div>
    <div class="abs tiny" style="left:13px;top:185px;width:74px">Lorem ipsum dolor sit amet, consectetur adipiscing elit, sed do eiusmod tempor incididunt ut labore et dolore magna aliqua. Ut enim ad minim veniam.</div>
    <div class="abs tiny" style="left:13px;top:208px;width:74px">Lorem ipsum dolor sit amet, consectetur adipiscing elit, sed do eiusmod tempor.</div>
    <div class="abs" style="left:13px;top:224px;width:74px;height:1px;background:var(--orange)"></div>
    <div class="abs tiny" style="left:15px;top:228px;width:72px;color:var(--orange)">Lorem ipsum dolor sit amet, consectetur adipiscing elit, sed do eiusmod tempor.</div>
    <div class="dot-blue" style="left:97px;top:205px">1</div>
    <div class="dot-blue" style="left:97px;top:212px">2</div>
    <div class="dot-blue" style="left:97px;top:221px">3</div>
    <div class="dot-blue" style="left:97px;top:231px">4</div>
    <div class="abs tiny" style="left:104px;top:206px">Lorem ipsum dolor sit amet, consectetur</div>
    <div class="abs tiny" style="left:104px;top:213px">Lorem ipsum dolor sit amet,</div>
    <div class="abs tiny" style="left:104px;top:221px">Lorem ipsum dolor sit amet, lorem ipsum<br>dolor sit amet, consectetur</div>
    <div class="abs tiny" style="left:104px;top:232px">Lorem ipsum dolor sit amet, consectetur</div>
    <div class="footer-band"></div><div class="footer-mark"></div>
    <div class="footer-text">NORVEL LASTING RESULTS<br>Lorem ipsum dolor sit amet | P: 12-123 1234 | E: info@xyx.com</div>
    <div class="footer-num">12</div>
  </section>

  <!-- BUDGET BREAKDOWN -->
  <section class="page" style="left:558px;top:314px;width:185px;height:261px">
    <div class="abs title" style="left:25px;top:14px">BUDGET<b>BREAKDOWN</b></div>
    <div class="abs" style="left:121px;top:13px;width:64px;height:20px;background:var(--sky);border-radius:10px 0 0 10px"></div>
    <div class="abs ghost-name" style="left:130px;top:17px;font-size:11px;color:#c5e4ef">NORVEL</div>
    <div class="abs tiny" style="left:45px;top:40px">Description</div>
    <div class="abs tiny" style="left:106px;top:40px">Plan 1</div>
    <div class="abs tiny" style="left:130px;top:40px">Plan 2</div>
    <div class="abs tiny" style="left:155px;top:40px">Plan 3</div>
    <svg class="abs" style="left:0;top:0" width="185" height="261" viewBox="0 0 185 261">
      <g fill="#addceb"><rect x="98" y="55" width="24" height="26"/><rect x="145" y="55" width="23" height="26"/><rect x="98" y="99" width="24" height="26"/><rect x="145" y="99" width="23" height="26"/><rect x="98" y="143" width="24" height="26"/><rect x="145" y="143" width="23" height="26"/><rect x="98" y="187" width="24" height="26"/><rect x="145" y="187" width="23" height="26"/><rect x="98" y="215" width="24" height="7"/><rect x="145" y="215" width="23" height="7"/></g>
      <g fill="#2aa9e0"><rect x="122" y="55" width="23" height="26"/><rect x="122" y="99" width="23" height="26"/><rect x="122" y="143" width="23" height="26"/><rect x="122" y="187" width="23" height="26"/><rect x="122" y="215" width="23" height="7"/></g>
      <g fill="#2aa9e0"><rect x="23" y="57" width="2" height="1"/><rect x="23" y="64" width="2" height="1"/><rect x="23" y="70" width="2" height="1"/><rect x="23" y="76" width="2" height="1"/><rect x="23" y="101" width="2" height="1"/><rect x="23" y="108" width="2" height="1"/><rect x="23" y="114" width="2" height="1"/><rect x="23" y="120" width="2" height="1"/><rect x="23" y="145" width="2" height="1"/><rect x="23" y="152" width="2" height="1"/><rect x="23" y="158" width="2" height="1"/><rect x="23" y="164" width="2" height="1"/><rect x="23" y="189" width="2" height="1"/><rect x="23" y="196" width="2" height="1"/><rect x="23" y="202" width="2" height="1"/><rect x="23" y="208" width="2" height="1"/></g>
    </svg>
    <div class="bar" style="left:19px;top:46px;width:149px;height:7px">Section Heading</div>
    <div class="bar" style="left:19px;top:90px;width:149px;height:7px">Section Heading</div>
    <div class="bar" style="left:19px;top:134px;width:149px;height:7px">Section Heading</div>
    <div class="bar" style="left:19px;top:178px;width:149px;height:7px">Section Heading</div>
    <div class="abs tiny" style="left:29px;top:55px;line-height:6.5px">Lorem ipsum dolor sit amet, consectetur<br>Lorem ipsum dolor sit amet, consectetur<br>Lorem ipsum dolor sit amet, consectetur<br>Lorem ipsum dolor sit amet, consectetur</div>
    <div class="abs tiny" style="left:29px;top:99px;line-height:6.5px">Lorem ipsum dolor sit amet, consectetur<br>Lorem ipsum dolor sit amet, consectetur<br>Lorem ipsum dolor sit amet, consectetur<br>Lorem ipsum dolor sit amet, consectetur</div>
    <div class="abs tiny" style="left:29px;top:143px;line-height:6.5px">Lorem ipsum dolor sit amet, consectetur<br>Lorem ipsum dolor sit amet, consectetur<br>Lorem ipsum dolor sit amet, consectetur<br>Lorem ipsum dolor sit amet, consectetur</div>
    <div class="abs tiny" style="left:29px;top:187px;line-height:6.5px">Lorem ipsum dolor sit amet, consectetur<br>Lorem ipsum dolor sit amet, consectetur<br>Lorem ipsum dolor sit amet, consectetur<br>Lorem ipsum dolor sit amet, consectetur</div>
    <div class="abs tiny" style="left:86px;top:217px;font-weight:700">Total</div>
    <div class="abs tiny" style="left:19px;top:232px;width:150px"><b>Note:</b> Lorem ipsum dolor sit amet, consectetur adipiscing elit, sed do eiusmod tempor incididunt ut labore et dolore magna aliqua. Ut enim ad minim veniam, quis nostrud exercitation ullamco laboris nisi ut aliquip ex ea.</div>
    <div class="footer-band"></div><div class="footer-mark"></div>
    <div class="footer-text">NORVEL LASTING RESULTS<br>Lorem ipsum dolor sit amet | P: 12-123 1234 | E: info@xyx.com</div>
    <div class="footer-num">12</div>
  </section>

  <!-- PROJECT INVOICE -->
  <section class="page" style="left:757px;top:314px;width:185px;height:261px">
    <div class="abs" style="left:19px;top:30px;font-size:8.5px;font-weight:300;color:#444">PROJECT <b style="font-weight:700;color:var(--orange)">INVOICE</b></div>
    <div class="abs" style="left:133px;top:13px;width:5px;height:5px;border-radius:50%;background:var(--blue)"></div>
    <div class="abs brand" style="left:140px;top:11px;font-size:7px">NORVEL</div>
    <div class="abs tiny" style="left:146px;top:20px">Street Address<br>City, ST ZIP Code<br>Phone<br>Fax<br>Email</div>
    <div class="abs tiny" style="left:19px;top:49px"><b>DATE:</b> Date</div>
    <div class="abs tiny" style="left:139px;top:49px"><b>INVOICE:</b> #####</div>
    <div class="abs small" style="left:22px;top:65px;font-weight:600;color:#333">Person Name</div>
    <div class="abs tiny" style="left:22px;top:74px">Lorem ipsum dolor sit amet, consectetur</div>
    <div class="abs small" style="left:22px;top:88px;font-weight:600;color:#333">Company Name</div>
    <div class="abs tiny" style="left:21px;top:97px">Street Address<br>City, ST ZIP Code<br>Phone<br>Fax<br>Email</div>
    <div class="bar" style="left:11px;top:134px;width:158px;height:7px;padding-left:19px">Section Heading</div>
    <div class="abs" style="left:104px;top:134px;width:65px;height:7px;background:#7fc8ea"></div>
    <svg class="abs" style="left:0;top:0" width="185" height="261" viewBox="0 0 185 261">
      <g stroke="#7fc8ea" stroke-width=".6" fill="none">
        <line x1="104" y1="141" x2="104" y2="191"/><line x1="122" y1="141" x2="122" y2="191"/><line x1="146" y1="141" x2="146" y2="191"/>
        <line x1="11" y1="161" x2="169" y2="161"/><line x1="11" y1="177" x2="169" y2="177"/><line x1="11" y1="191" x2="169" y2="191"/>
      </g>
      <rect x="15" y="152" width="2" height=".8" fill="#2aa9e0"/>
    </svg>
    <div class="abs tiny" style="left:107px;top:136px;color:#fff">dolor sit &nbsp;&nbsp;&nbsp;&nbsp; dolor sit &nbsp;&nbsp;&nbsp;&nbsp; dolor sit</div>
    <div class="abs tiny" style="left:22px;top:151px">Lorem ipsum dolor sit amet, consectetur</div>
    <div class="abs tiny" style="left:107px;top:151px">dolor sit &nbsp;&nbsp;&nbsp;&nbsp; dolor sit &nbsp;&nbsp;&nbsp;&nbsp; dolor sit</div>
    <div class="abs small" style="left:22px;top:207px;font-weight:600;color:#333">Person Name</div>
    <div class="abs tiny" style="left:21px;top:215px">Lorem ipsum dolor sit amet, lorem ipsum<br>dolor sit amet, consectetur</div>
    <div class="abs" style="left:11px;top:232px;width:158px;height:7px;background:var(--orange);color:#fff;font-size:2.8px;line-height:7px;text-align:center">Lorem ipsum dolor sit amet, consectetur</div>
    <div class="footer-band"></div><div class="footer-mark"></div>
    <div class="footer-text">NORVEL LASTING RESULTS<br>Lorem ipsum dolor sit amet | P: 12-123 1234 | E: info@xyx.com</div>
    <div class="footer-num">12</div>
  </section>

  <!-- HEADING TO BE WITH US -->
  <section class="page" style="left:958px;top:314px;width:185px;height:261px">
    <div class="abs ghost-name" style="left:17px;top:8px;font-size:13px;color:#eeeeee">NORVEL</div>
    <div class="abs" style="left:28px;top:29px;width:157px;height:71px;background:var(--sky);border-radius:12px 0 0 12px"></div>
    <div class="photo" role="img" aria-label="Photo of water pouring onto young plants" style="left:113px;top:0;width:53px;height:80px;border-radius:0 0 10px 10px;background:linear-gradient(180deg,#c4873a,#5e5a2e 50%,#2f3a1f)"></div>
    <div class="abs" style="left:38px;top:51px;font-size:8px;line-height:8.6px;font-weight:300;color:#444">HEADING<br>TO BE<br>WITH US</div>
    <div class="abs" style="left:20px;top:106px;font-size:8px;font-weight:300;color:#333"><b style="font-weight:700">HEADING</b> TO BE WITH US</div>
    <div class="drop" style="left:13px;top:121px"></div><div class="drop" style="left:13px;top:129px"></div><div class="drop" style="left:13px;top:139px"></div><div class="drop" style="left:13px;top:149px"></div><div class="drop" style="left:13px;top:159px"></div>
    <div class="abs tiny" style="left:21px;top:122px;line-height:3.4px">Lorem ipsum dolor sit amet, consectetur<br><br>Lorem ipsum dolor sit amet,<br><br>Lorem ipsum dolor sit amet, Lorem ipsum<br>dolor sit amet, consectetur<br><br>Lorem ipsum dolor sit amet, consectetur<br><br>Lorem ipsum dolor</div>
    <div class="drop" style="left:92px;top:121px"></div><div class="drop" style="left:92px;top:129px"></div><div class="drop" style="left:92px;top:139px"></div><div class="drop" style="left:92px;top:149px"></div><div class="drop" style="left:92px;top:159px"></div>
    <div class="abs tiny" style="left:100px;top:122px;line-height:3.4px">Lorem ipsum dolor sit amet, consectetur<br><br>Lorem ipsum dolor sit amet, consectetur<br><br>Lorem ipsum dolor sit amet, Lorem ipsum<br>dolor sit amet, consectetur<br><br>Lorem ipsum dolor sit amet, consectetur<br><br>Lorem ipsum dolor sit amet, Lorem ipsum</div>
    <div class="photo" role="img" aria-label="Photo of glass office towers" style="left:0;top:178px;width:86px;height:50px;border-radius:0 8px 8px 0;background:linear-gradient(180deg,#b8d3e6,#5f8fb2 60%,#2e4e6a)"></div>
    <div class="abs" style="left:92px;top:180px;width:74px;height:1px;background:var(--blue)"></div>
    <div class="abs tiny" style="left:92px;top:186px;width:74px">Lorem ipsum dolor sit amet, consectetur adipiscing elit, sed do eiusmod tempor incididunt ut labore et dolore magna aliqua. Ut enim ad minim veniam, quis nostrud exercitation ullamco laboris nisi ut aliquip ex ea.</div>
    <div class="abs tiny" style="left:92px;top:210px;width:74px">Lorem ipsum dolor sit amet, consectetur adipiscing elit, sed do eiusmod tempor incididunt ut labore et dolore magna aliqua.</div>
    <div class="footer-band"></div><div class="footer-mark"></div>
    <div class="footer-text">NORVEL LASTING RESULTS<br>Lorem ipsum dolor sit amet | P: 12-123 1234 | E: info@xyx.com</div>
    <div class="footer-num">12</div>
  </section>

  <!-- THE END -->
  <section class="page" style="left:730px;top:602px;width:228px;height:323px">
    <svg class="abs" style="left:0;top:0" width="228" height="323" viewBox="0 0 228 323">
      <path d="M0 0H77V60Q77 68 70 71L0 81Z" fill="#addceb"/>
      <g role="img" aria-label="Photo of modern building with a tree">
        <path d="M0 120L100 62Q118 55 119 70V96Q119 104 110 109L0 170Z" fill="url(#bld)"/>
      </g>
      <g role="img" aria-label="Photo of timber slat facade">
        <path d="M0 176L70 140Q100 128 100 148V186Q100 196 90 200L0 240Z" fill="url(#wood)"/>
      </g>
      <g role="img" aria-label="Warm photo of a tree against a building">
        <path d="M110 126L228 69V150L128 182Q110 188 110 170Z" fill="url(#tree)"/>
      </g>
      <defs>
        <linearGradient id="bld" x1="0" y1="1" x2="1" y2="0"><stop offset="0" stop-color="#3a3a36"/><stop offset=".6" stop-color="#9aa08e"/><stop offset="1" stop-color="#6f8a4a"/></linearGradient>
        <linearGradient id="wood" x1="0" y1="0" x2="1" y2="1"><stop offset="0" stop-color="#5a4a36"/><stop offset=".5" stop-color="#b08850"/><stop offset="1" stop-color="#d1a56a"/></linearGradient>
        <linearGradient id="tree" x1="0" y1="1" x2="1" y2="0"><stop offset="0" stop-color="#8a6a34"/><stop offset=".6" stop-color="#c99a55"/><stop offset="1" stop-color="#f0dcc0"/></linearGradient>
      </defs>
    </svg>
    <div class="abs brand" style="left:20px;top:28px;font-size:8px">NORVEL</div>
    <div class="abs" style="left:20px;top:38px;font-size:2.8px;color:var(--blue)">ENGINEERED LASTING RESULTS</div>
    <div class="abs" style="left:115px;top:229px;font-size:16px;font-weight:300;color:#333">THE <b style="font-weight:700;color:#222">END</b></div>
    <div class="abs" style="left:32px;top:265px;font-size:7px;font-weight:700;color:#cfcfcf;letter-spacing:.5px">NORVEL</div>
    <div class="meta-line" style="left:29px;top:279px;height:7px"></div>
    <div class="abs" style="left:33px;top:281px;font-size:3.6px;color:#555">NORVEL LASTING RESULTS</div>
    <div class="meta-line" style="left:29px;top:293px;height:14px"></div>
    <div class="abs" style="left:33px;top:293px;font-size:3.6px;line-height:4.6px;color:#555">Lorem ipsum dolor sit amet<br>P: 12-123 1234<br>E: info@xyx.com</div>
  </section>

  <div class="stage-name">NORVEL</div>
</div>
</body>
</html>
```